Consultancy company needs flyer design

We need a flyer design for a new service to be provided. It is a service in which project management is outsourced. Text of the service has been attached (in Dutch).
We would like the design to be in line with our website design (www.velostrin.com). Also we would like to re-use the main banner of the site (see attachment)

Industry/Entity Type

It Company

Requirements
Must have
• Flyer must be double sided

```html
<!DOCTYPE html>
<html lang="nl">
<head>
<meta charset="utf-8">
<title>Velostrin – Project Management As a Service flyer</title>
<link rel="stylesheet" href="https://fonts.googleapis.com/css2?family=Open+Sans:wght@400;600;700&display=swap">
<style>
  :root {
    --bg: #e4e1dd;
    --paper: #ffffff;
    --ink: #2a2623;
    --brown: #5a3d23;
    --taupe-light: #c9c0b6;
    --taupe: #9c9084;
    --steel-light: #8d8985;
    --steel-dark: #3f3b38;
    --band-dark: #1a1614;
    --gold: #8a6a3e;
  }
  * { margin: 0; padding: 0; box-sizing: border-box; }
  html, body { width: 1200px; height: 800px; overflow: hidden; }
  body {
    background: var(--bg);
    font-family: "Open Sans", sans-serif;
    color: var(--ink);
    position: relative;
  }
  .flyer {
    position: absolute;
    top: 18px;
    width: 540px;
    height: 764px;
    background: var(--paper);
    box-shadow: 0 4px 14px rgba(0,0,0,.18);
    overflow: hidden;
  }
  .flyer--front { left: 45px; }
  .flyer--back { left: 615px; }

  .brand {
    position: absolute;
    display: flex;
    align-items: center;
    gap: 8px;
    z-index: 3;
  }
  .brand__mark {
    width: 30px; height: 30px;
    background: var(--brown);
  }
  .brand__name {
    font-size: 26px;
    font-weight: 600;
    color: var(--ink);
    letter-spacing: .5px;
  }
  .flyer--front .brand { left: 42px; top: 22px; }
  .flyer--back .brand { left: 34px; top: 26px; }

  .photo-band { position: absolute; left: 0; z-index: 1; }
  .flyer--front .photo-band { top: 0; }
  .flyer--back .photo-band { top: 0; }

  .intro-box {
    position: absolute;
    left: 58px; top: 92px;
    width: 240px; height: 178px;
    background: var(--paper);
    padding: 12px 14px;
    z-index: 2;
  }
  .intro-box__kicker { font-size: 9px; font-weight: 700; }
  .intro-box__title {
    font-size: 14.5px; font-weight: 700; line-height: 1.15; margin-top: 3px;
  }
  .rule {
    display: block; width: 34px; height: 2px; background: var(--brown);
    margin: 5px 0 7px;
  }
  .intro-box__text { font-size: 8.5px; line-height: 1.35; text-align: justify; }

  .issue-band {
    position: absolute;
    left: 0; top: 286px; width: 540px; height: 82px;
    background: linear-gradient(180deg, var(--taupe) 0%, var(--taupe-light) 100%);
    padding: 12px 40px 0 52px;
  }
  .list { list-style: none; font-size: 8.5px; line-height: 1.38; }
  .list li::before { content: "• "; }

  .front-body {
    position: absolute;
    left: 42px; top: 382px; width: 460px;
    font-size: 8.5px; line-height: 1.36;
  }
  .front-body p { text-align: justify; }
  .front-body .rule { margin: 0 0 5px; }
  .section-title { font-size: 9.5px; font-weight: 700; margin-top: 9px; }
  .front-body .list { margin-top: 2px; }
  .summary { font-weight: 700; font-size: 9px; margin-top: 8px; }

  .foot-band {
    position: absolute; left: 0; bottom: 0; width: 540px; height: 34px;
    background: var(--band-dark);
    border-top: 5px solid var(--gold);
  }

  .back-body {
    position: absolute;
    left: 40px; top: 470px; width: 462px;
    font-size: 8.7px; line-height: 1.4;
  }
  .back-body .section-title { margin-top: 0; }
  .back-body .rule { margin: 3px 0 6px; }
  .back-body p { text-align: justify; }
  .contact {
    position: absolute;
    left: 40px; top: 600px;
    border-left: 2px solid var(--brown);
    padding-left: 8px;
    font-size: 12px; line-height: 1.38;
  }
  .contact b { font-weight: 700; }
</style>
</head>
<body>

<!-- Front side -->
<section class="flyer flyer--front">
  <div class="brand"><span class="brand__mark"></span><span class="brand__name">velostrin</span></div>

  <svg class="photo-band" width="540" height="300" viewBox="0 0 540 300" role="img" aria-label="Photograph of steel gears and cogwheels">
    <defs>
      <linearGradient id="steelFront" x1="0" y1="0" x2="1" y2="1">
        <stop offset="0" stop-color="#6e6a66"/>
        <stop offset=".5" stop-color="#9a9590"/>
        <stop offset="1" stop-color="#4a4643"/>
      </linearGradient>
    </defs>
    <path d="M0 95 C120 60 300 72 540 40 L540 300 L0 300 Z" fill="url(#steelFront)"/>
    <path d="M0 250 C180 300 360 250 540 270 L540 300 L0 300 Z" fill="#9c9084"/>
    <path d="M0 82 C120 48 300 62 540 28" fill="none" stroke="#1a1614" stroke-width="6"/>
  </svg>

  <div class="intro-box">
    <div class="intro-box__kicker">Ontzorging van uw projectdelivery:</div>
    <h1 class="intro-box__title">Project Management<br>As a Service(PMAAS)</h1>
    <span class="rule"></span>
    <p class="intro-box__text">U kunt voor de realisatie van uw projectportfolio de hulp inroepen van externe projectmanagers, en daarbij zelf de coördinatie verzorgen. Grote kans dat u dan tegen één of meer van de volgende zaken aan loopt:</p>
  </div>

  <div class="issue-band">
    <ul class="list">
      <li>Een wisselende kwaliteit van projectmanagers</li>
      <li>Problemen om kosten inzichtelijk en voorspelbaar of beheersbaar houden (management rapportage)</li>
      <li>Een ad hoc relatie met uw projectmanagers en leveranciers</li>
      <li>Beperkt leergedrag en herhaling van fouten</li>
      <li>Tijdverlies en kosten omdat u veel tijd kwijt bent aan uitleg van rand voorwaardelijke zaken</li>
    </ul>
  </div>

  <div class="front-body">
    <span class="rule"></span>
    <p>Een alternatief is onze PMAAS-service. Die bevat alle ingrediënten om uw projectenportfolio kostenefficiënt en op hoog kwaliteitsniveau te realiseren. Velostrin zorgt voor inzet van projectmanagers die al 'up to speed' zijn als ze bij u binnenkomen. Ze hebben de juiste expertise, zijn al ingewerkt op uw of onze standaard methodiek en op uw organisatorische setting. En heeft u ineens meer of minder werk? Geen probleem. Dan schalen wij net zo gemakkelijk op en af.</p>

    <h2 class="section-title">Wij zorgen voor</h2>
    <span class="rule"></span>
    <ul class="list">
      <li>een eenduidige werkwijze, rapportering en gebruik van tooling</li>
      <li>een scherpe intake en voorbereidingsfase van de te starten projecten</li>
      <li>de benodigde op-en afschaling van project managers met het juiste profiel</li>
      <li>ingewerkte projectmanagers op de overeengekomen projectmethode</li>
      <li>continue monitoring op afgesproken KPI's over de projecten heen</li>
      <li>periodiek overleg over de performance</li>
      <li>continue verbetering op basis van klantevaluaties</li>
      <li>facturatie volgens afspraak (milestone-based)</li>
    </ul>

    <h2 class="section-title">U zorgt voor:</h2>
    <span class="rule"></span>
    <ul class="list">
      <li>een up to date forecast van de te realiseren projectportfolio</li>
      <li>een goede projectbrief als basis voor onze intake</li>
    </ul>

    <p class="summary">Kortom: laat u ontzorgen in uw project delivery!</p>

    <h2 class="section-title">PMO en PPM</h2>
    <span class="rule"></span>
    <p>Wilt u zich nog meer laten ontzorgen? Dat kan! Naast onze PMAAS-service leveren wij ook diensten op het gebied van Project Management Office (PMO) en/of Project Portfolio Management (PPM). Wij kunnen deze activiteiten voor u opzetten, maar ook de operationele aansturing ervan ondersteunen of voor onze rekening</p>
  </div>

  <div class="foot-band"></div>
</section>

<!-- Back side -->
<section class="flyer flyer--back">
  <div class="brand"><span class="brand__mark"></span><span class="brand__name">velostrin</span></div>

  <svg class="photo-band" width="540" height="440" viewBox="0 0 540 440" role="img" aria-label="Photograph of large steel gears with a roller chain">
    <defs>
      <linearGradient id="steelBack" x1="0" y1="0" x2="1" y2="1">
        <stop offset="0" stop-color="#5a5652"/>
        <stop offset=".45" stop-color="#a29d98"/>
        <stop offset="1" stop-color="#3f3b38"/>
      </linearGradient>
    </defs>
    <path d="M0 112 C150 80 340 82 540 30 L540 345 C380 380 200 330 0 420 Z" fill="url(#steelBack)"/>
    <path d="M0 100 C150 68 340 70 540 18" fill="none" stroke="#1a1614" stroke-width="6"/>
  </svg>

  <div class="back-body">
    <h2 class="section-title">Velostrin: innovatief in verandertrajecten</h2>
    <span class="rule"></span>
    <p>Als management consultancy bureau houden wij ons bezig met de begeleiding van veranderingen in bedrijven. Op het gebied van strategie, maar ook van processen en systemen. Wij onderscheiden ons door toepassing van visualisatie technieken, bedrijfsproces simulaties en unieke services en zijn continu op zoek naar nieuwe toepassingsmogelijkheden op dit gebied. Door de krachten van uw medewerkers en die van ons te verenigen, komen we tot betere en snellere resultaten. Daarbij gaan wij samen op reis. Want veranderingen kun je niet leren, je moet ze ervaren.</p>
  </div>

  <div class="contact">
    Meer weten<br>
    Wilt u meer weten, bekijk onze<br>
    Of bel of mail ons<br>
    <b>website:</b> www.velostrin.com<br>
    <b>Telefoon:</b> 085 - 0047719<br>
    <b>E-mail:</b> info@velostrin.com
  </div>

  <div class="foot-band"></div>
</section>

</body>
</html>
```